KV HOLDING Business Cards

I need business cards for "KV Holding group LLC" doublesided... logo on the back (also include logo on front)
logo attached to project... i have jpg up..
Company Info:
418 East Marlow Avenue, Suite 7B
Chicago, Illinois 60617
facsimile 312-555-0188 (list fax, address, website on all cards.)
www.kvholdinggroup.example
Three different people on cards:
Dorian P. Kell, CPA MST
Principal
ofc 312-555-0142
mobile 312-555-0167
dorianpkell@kvholdinggroup.example
Marcus T. Brenholt, CPA MST
Principal
marcustbrenholt@kvholdinggroup.example
mobile 708-555-0119
ofc 312-555-0142
Nigel F Carrow
Principal
ofc 312-555-0142
no mobile
nigelfcarrow@kvholdinggroup.example
I have multiple projects listed.. see below:
Business cards for amber gate equity llc
letterhead
envelopes
Business cards for KV Holding LLC
letterhead
envelopes
Target Market(s)
rich people
Industry/Entity Type
Business
Look and feel

```html
<!DOCTYPE html>
<html lang="en">
<head>
<meta charset="utf-8">
<title>KV Holding Group LLC – Business Cards</title>
<link rel="stylesheet" href="https://fonts.googleapis.com/css2?family=Montserrat:wght@400;500;700&display=swap">
<style>
  :root {
    --brand-blue: #2f4f8e;
    --brand-blue-deep: #27447c;
    --frame-line: #6f8cc4;
    --paper: #ffffff;
    --paper-shade: #f1f2f4;
    --ink: #3a3f4a;
    --backdrop: #e3e3e3;
  }
  * { box-sizing: border-box; margin: 0; padding: 0; }
  html, body { width: 1200px; height: 908px; overflow: hidden; }
  body {
    background: var(--backdrop);
    font-family: "Montserrat", sans-serif;
    position: relative;
  }

  .card {
    position: absolute;
    width: 560px;
    height: 320px;
    box-shadow: 0 10px 26px rgba(0,0,0,0.18);
    overflow: hidden;
  }

  /* Back side */
  .card-back {
    left: 150px;
    top: 110px;
    background: var(--brand-blue);
  }
  .card-back .inner-frame {
    position: absolute;
    inset: 14px;
    border: 2px solid var(--frame-line);
  }
  .card-back .brand-mark {
    position: absolute;
    inset: 0;
    display: flex;
    align-items: center;
    justify-content: center;
    gap: 14px;
  }
  .brand-mark .mark-dot {
    width: 34px; height: 34px;
    border-radius: 50%;
    background: var(--paper);
  }
  .brand-mark .mark-name {
    color: var(--paper);
    font-weight: 500;
    font-size: 28px;
    letter-spacing: 4px;
  }

  /* Front side */
  .card-front {
    left: 490px;
    top: 470px;
    background: linear-gradient(180deg, var(--paper) 0%, var(--paper-shade) 100%);
  }
  .front-logo {
    position: absolute;
    left: 36px; top: 34px;
    display: flex; align-items: center; gap: 10px;
  }
  .front-logo .mark-dot {
    width: 22px; height: 22px; border-radius: 50%;
    background: var(--brand-blue);
  }
  .front-logo .mark-name {
    color: var(--brand-blue);
    font-weight: 500;
    font-size: 13px;
    letter-spacing: 2px;
  }

  .name-block {
    position: absolute;
    left: 36px; top: 92px;
    width: 250px;
    background: var(--brand-blue);
    color: var(--paper);
    padding: 12px 16px;
  }
  .name-block .person-name {
    font-size: 21px; font-weight: 700; letter-spacing: 0.5px;
    white-space: nowrap;
  }
  .name-block .person-name .surname { font-weight: 400; }
  .name-block .person-role {
    font-size: 14px; font-weight: 400; margin-top: 2px;
  }

  .contact-list {
    position: absolute;
    list-style: none;
    color: var(--ink);
    font-size: 11px;
    line-height: 1.5;
    white-space: nowrap;
  }
  .contact-phones { left: 52px; top: 172px; }
  .contact-web { left: 302px; top: 100px; }
  .contact-address { left: 302px; top: 152px; }

  .contact-band {
    position: absolute;
    left: 0; right: 0; bottom: 0;
    height: 74px;
  }
  .contact-band svg { display: block; }
</style>
</head>
<body>

  <section class="card card-back" aria-label="Card back">
    <div class="inner-frame"></div>
    <div class="brand-mark">
      <span class="mark-dot"></span>
      <span class="mark-name">KV HOLDING</span>
    </div>
  </section>

  <section class="card card-front" aria-label="Card front">
    <div class="front-logo">
      <span class="mark-dot"></span>
      <span class="mark-name">KV HOLDING GROUP LLC</span>
    </div>

    <div class="name-block">
      <div class="person-name">DORIAN P. <span class="surname">KELL</span></div>
      <div class="person-role">Principal, CPA MST</div>
    </div>

    <ul class="contact-list contact-phones">
      <li>ofc 312-555-0142</li>
      <li>mobile 312-555-0167</li>
      <li>fax 312-555-0188</li>
    </ul>

    <ul class="contact-list contact-web">
      <li>dorianpkell@kvholdinggroup.example</li>
      <li>www.kvholdinggroup.example</li>
    </ul>

    <ul class="contact-list contact-address">
      <li>418 East Marlow Avenue, Suite 7B</li>
      <li>Chicago, Illinois 60617</li>
    </ul>

    <div class="contact-band">
      <svg width="560" height="74" viewBox="0 0 560 74">
        <polygon points="0,26 560,10 560,74 0,74" fill="var(--brand-blue)"/>
        <polygon points="0,26 560,10 560,16 0,32" fill="var(--brand-blue-deep)"/>
        <g transform="translate(70,46)">
          <circle r="13" fill="var(--paper)"/>
          <path d="M-5,-6 q-2,0 -2,3 q1,8 10,10 q3,0 3,-2 l-3,-3 l-2,1 q-4,-2 -5,-5 l1,-2 z" fill="var(--brand-blue)"/>
        </g>
        <g transform="translate(318,42)">
          <circle r="13" fill="var(--paper)"/>
          <circle r="7" fill="none" stroke="var(--brand-blue)" stroke-width="1.5"/>
          <ellipse rx="3" ry="7" fill="none" stroke="var(--brand-blue)" stroke-width="1.2"/>
          <line x1="-7" y1="0" x2="7" y2="0" stroke="var(--brand-blue)" stroke-width="1.2"/>
        </g>
        <g transform="translate(470,38)">
          <circle r="13" fill="var(--paper)"/>
          <path d="M0,8 C-5,2 -6,-1 -6,-3 A6,6 0 0 1 6,-3 C6,-1 5,2 0,8 Z" fill="var(--brand-blue)"/>
          <circle cy="-3" r="2" fill="var(--paper)"/>
        </g>
      </svg>
    </div>
  </section>

</body>
</html>
```